Stationery for Public Accountant Practice

Name of Practice
Holloway Merrick Pty Ltd
Tel: 0413927056
Postal Address : PO Box 482, Oakvale East, Vic 3187

Target Market(s)

Small Business Clients

Industry/Entity Type

Accounting

Font styles to use
Serif

Requirements
Must have
• Letterhead, business card, With compliments slip
Nice to have
• Conservative

```html
<!DOCTYPE html>
<html lang="en">
<head>
<meta charset="utf-8">
<title>Holloway Merrick Pty Ltd — Letterhead</title>
<link rel="stylesheet" href="https://fonts.googleapis.com/css2?family=Cinzel:wght@500&family=Didact+Gothic&display=swap">
<style>
  :root {
    --backdrop: #d1d1d1;
    --paper: #f0f0f0;
    --ink: #2b2b2b;
    --ink-soft: #3a3a3a;
    --gold: #c0973a;
    --gold-light: #e2b655;
    --gold-deep: #a97f2c;
    --band-dark: #444444;
  }
  * { margin: 0; padding: 0; box-sizing: border-box; }
  html, body {
    width: 1200px; height: 1041px; overflow: hidden;
    background: var(--backdrop);
  }
  .letterhead {
    position: absolute; left: 278px; top: 103px;
    width: 645px; height: 835px;
    background: var(--paper);
  }
  .brand { position: absolute; left: 54px; top: 55px; display: flex; align-items: flex-start; }
  .brand-mark {
    width: 36px; height: 36px; margin-right: 10px; margin-top: 1px;
    background: var(--gold);
  }
  .brand-name {
    font-family: "Cinzel", serif; font-weight: 500;
    font-size: 20px; line-height: 22px; color: var(--ink);
    letter-spacing: 0.2px;
    white-space: nowrap;
  }
  .brand-name .entity { font-size: 8px; letter-spacing: 0; }
  .brand-rule { height: 1px; width: 242px; background: var(--ink-soft); margin-top: 3px; }
  .brand-tagline {
    font-family: "Cinzel", serif; font-weight: 500;
    font-size: 9.6px; line-height: 12px; color: var(--ink);
    margin-top: 2px; letter-spacing: 0.1px; white-space: nowrap;
  }
  .contact {
    position: absolute; left: 433px; top: 57px;
    font-family: "Didact Gothic", sans-serif; font-size: 9px; line-height: 11.5px; color: var(--ink);
  }
  .contact-line { display: flex; align-items: center; height: 11.5px; }
  .contact-line svg { width: 9px; height: 9px; margin-right: 6px; flex: none; }
  .postal { margin-top: 6px; }
  .footer-band { position: absolute; left: 0; bottom: 0; width: 645px; height: 16px; }
</style>
</head>
<body>
  <main class="letterhead">
    <header class="brand">
      <div class="brand-mark"></div>
      <div class="brand-text">
        <div class="brand-name">Holloway Merrick <span class="entity">Pty Ltd</span></div>
        <div class="brand-rule"></div>
        <div class="brand-tagline">CERTIFIED PRACTISING ACCOUNTANTS</div>
      </div>
    </header>

    <address class="contact" style="font-style:normal">
      <div class="contact-line">
        <svg viewBox="0 0 10 10" aria-hidden="true"><rect width="10" height="10" rx="1.5" fill="var(--gold)"/><path d="M3 2.2c.4-.3.8-.2 1 .2l.5 1c.1.3 0 .6-.2.8l-.3.3c.3.7.8 1.2 1.5 1.5l.3-.3c.2-.2.5-.3.8-.2l1 .5c.4.2.5.6.2 1-.5.7-1.3.9-2.1.5C4.3 6.7 3.3 5.7 2.5 4.3c-.4-.8-.2-1.6.5-2.1z" fill="#fff"/></svg>
        <span>0413927056</span>
      </div>
      <div class="contact-line">
        <svg viewBox="0 0 10 10" aria-hidden="true"><rect width="10" height="10" rx="1.5" fill="var(--gold)"/><rect x="2" y="3" width="6" height="4.2" fill="none" stroke="#fff" stroke-width=".8"/><path d="M2 3l3 2.3L8 3" fill="none" stroke="#fff" stroke-width=".8"/></svg>
        <span>daniel@hollowaymerrick.com.au</span>
      </div>
      <div class="postal">
        <div>PO Box 482</div>
        <div>Oakvale East, Vic 3187</div>
      </div>
    </address>

    <svg class="footer-band" viewBox="0 0 645 16" preserveAspectRatio="none" aria-hidden="true">
      <defs>
        <linearGradient id="goldBand" x1="0" x2="1" y1="0" y2="0">
          <stop offset="0" stop-color="var(--gold-deep)"/>
          <stop offset="0.55" stop-color="var(--gold-light)"/>
          <stop offset="1" stop-color="var(--gold-deep)"/>
        </linearGradient>
      </defs>
      <polygon points="0,6 424,6 415,16 0,16" fill="var(--band-dark)"/>
      <polygon points="428,6 432,6 422,16 418,16" fill="#ffffff"/>
      <polygon points="438,1 645,1 645,16 424,16" fill="url(#goldBand)"/>
    </svg>
  </main>
</body>
</html>
```